Website design for a personal and professional coaching firm

We need a website design of at least 5 pages for a personal and professional life and leadership Coaching and Life Services Firm. Main Interest: life, relationships and career.
Family, personal development, professional development. Companies and corporations
CHK OUT FACEBOOK PAGE: OREMBY PATH HOUSE Coaching and Life Services
Target Market(s)
Our Target Audience:
25 to 55 year old men and women living in city, suburbs, and some rural areas. Income from 50k and above. Young professionals, middle of career, college degree. Company, corporate, government, human resources sensitive industries.
Industry/Entity Type
Life Coaching
Number of Pages Required
5+ page
Requirements
Must have
- #1 - relevance/in touch
- #2 - creativity
- #3 - connection with them
Should not have
- the least amount of scrolling the better. Simple, clean and user friendly website not loaded down with a ton of reading

```html
<!DOCTYPE html>
<html lang="en">
<head>
<meta charset="utf-8">
<title>Oremby Path House — Coaching and Life Services</title>
<link href="https://fonts.googleapis.com/css2?family=Lato:wght@300;400;700&display=swap" rel="stylesheet">
<style>
  :root{
    --green:#2fb24a;
    --blue:#0a43b4;
    --ink:#2b2b2b;
    --muted:#5f5f5f;
    --band:#f5f4f0;
    --quote-band:#faf9f7;
    --page:#ffffff;
    --header:#f9f8f6;
  }
  *{box-sizing:border-box;margin:0;padding:0}
  html,body{width:1093px;height:1200px;overflow:hidden;background:var(--page)}
  body{font-family:'Lato',sans-serif;color:var(--ink);position:relative}
  .abs{position:absolute}

  .site-header{position:absolute;left:0;top:0;width:1093px;height:99px;background:var(--header)}
  .topbar{font-size:8px;letter-spacing:.2px;color:#333;top:6px}
  .topbar.left{left:90px;display:flex;gap:10px}
  .topbar.right{left:716px;display:flex;gap:10px;align-items:center}
  .social{display:flex;gap:9px;align-items:center}
  .social span{display:block;width:7px;height:7px;border-radius:50%;background:#555}

  .brand{left:92px;top:40px;display:flex;align-items:center;gap:8px}
  .brand-mark{width:14px;height:14px;border-radius:50%;background:var(--blue)}
  .brand-name{font-size:15px;font-weight:700;color:var(--blue);letter-spacing:1px}

  .main-nav{top:46px;left:495px;display:flex;gap:24px;font-size:11px;color:#444;letter-spacing:.1px}

  .book-btn{left:950px;top:72px;width:52px;height:52px;border-radius:50%;background:var(--blue);display:flex;align-items:center;justify-content:center;z-index:3}

  .hero{left:0;top:99px;width:1079px;height:420px;background:linear-gradient(100deg,#3c3a3e 0%,#6b5f5a 30%,#8a7566 50%,#5a4a40 72%,#2e2c30 100%)}
  .hero-edge{left:0;top:99px;width:198px;height:4px;background:#777}
  .hero-kicker{left:156px;top:226px;font-size:14px;color:#b9b2ab}
  .hero-title{left:156px;top:283px;font-size:48px;line-height:53px;font-weight:700;color:#fff}
  .hero-cta{left:156px;top:430px;font-size:11px;font-weight:700;color:var(--green);padding-bottom:4px;border-bottom:2px solid var(--green)}

  .services{left:0;top:520px;width:1093px;height:261px;background:var(--band)}
  .service{position:absolute;top:48px;width:210px}
  .service svg{display:block}
  .service h3{margin-top:28px;font-size:18px;font-weight:400;color:var(--green)}
  .service p{margin-top:14px;font-size:12.5px;line-height:18px;color:var(--muted)}
  .service .more{margin-top:8px;display:block}

  .testimonial{left:0;top:781px;width:1093px;height:174px;background:var(--quote-band);text-align:center}
  .testimonial blockquote{width:580px;margin:55px auto 0;font-size:14.5px;line-height:20px;color:#555}
  .testimonial cite{display:block;margin-top:12px;font-style:normal;font-size:9.5px;font-weight:700;color:var(--green)}

  .about-title{left:90px;top:1018px;font-size:30px;font-weight:300;color:var(--green)}
  .portrait{left:130px;top:1095px;width:360px;height:360px;border-radius:50%;background:linear-gradient(180deg,#d9d6d8 0%,#b9b3b2 60%,#7a6e6a 100%)}
  .profile-name{left:558px;top:1110px;font-size:21px;color:#222}
  .profile-role{left:558px;top:1141px;font-size:13px;color:#333}
  .profile-bio{left:558px;top:1180px;width:440px;font-size:13px;line-height:18px;color:#555}
</style>
</head>
<body>
  <header class="site-header">
    <div class="abs topbar left"><span>➜ LOGIN</span><span>✎ REGISTER</span></div>
    <div class="abs topbar right">
      <span>✉ hello@orembypath.com</span>
      <span>☎ 555-014-2207</span>
      <div class="social" aria-label="Social links"><span></span><span></span><span></span><span></span><span></span><span></span></div>
    </div>
    <div class="abs brand"><span class="brand-mark"></span><span class="brand-name">OREMBY PATH HOUSE</span></div>
    <nav class="abs main-nav"><span>HOME</span><span>ABOUT ME</span><span>CHANGE YOUR LIFE</span><span>WORKSHOPS</span><span>SHOP</span><span>BLOG</span><span>MEET ME</span></nav>
  </header>

  <a class="abs book-btn" aria-label="Book a session">
    <svg width="20" height="18" viewBox="0 0 20 18" fill="none" stroke="#fff" stroke-width="2"><rect x="1" y="3" width="18" height="14" rx="1"/><line x1="1" y1="7" x2="19" y2="7"/><line x1="6" y1="0" x2="6" y2="4"/><line x1="14" y1="0" x2="14" y2="4"/></svg>
  </a>

  <section class="abs hero" role="img" aria-label="Photo of a seminar audience watching a speaker"></section>
  <div class="abs hero-edge"></div>
  <p class="abs hero-kicker">I will tell you how to</p>
  <h1 class="abs hero-title">Restart Your Career<br>To Be more Successful</h1>
  <a class="abs hero-cta">TELL ME HOW</a>

  <section class="abs services">
    <div class="service" style="left:90px">
      <svg width="46" height="42" viewBox="0 0 46 42" fill="none" stroke="var(--green)" stroke-width="2.4"><path d="M23 3C11 3 2 10 2 19c0 5 3 9 7 12l-3 8 9-5c3 1 5 1 8 1 12 0 21-7 21-16S35 3 23 3z"/></svg>
      <h3>My Mentoring</h3>
      <p>Fusce facilisis nec ante et accumsan. Ut malesuada tristique sagittis</p>
      <svg class="more" width="18" height="10" viewBox="0 0 18 10" fill="none" stroke="#222" stroke-width="1.3"><line x1="1" y1="5" x2="16" y2="5"/><polyline points="12,1 16,5 12,9"/></svg>
    </div>
    <div class="service" style="left:324px">
      <svg width="46" height="46" viewBox="0 0 46 46" fill="none" stroke="var(--green)" stroke-width="2.4"><rect x="2" y="10" width="42" height="34"/><rect x="18" y="2" width="10" height="12"/><circle cx="12" cy="26" r="3"/><path d="M7 38c0-5 10-5 10 0"/><line x1="22" y1="24" x2="38" y2="24"/><line x1="22" y1="30" x2="38" y2="30"/><line x1="22" y1="36" x2="38" y2="36"/></svg>
      <h3 style="margin-top:24px">Successful Stories</h3>
      <p>Fusce facilisis nec ante et accumsan. Ut malesuada tristique sagittis</p>
      <svg class="more" width="18" height="10" viewBox="0 0 18 10" fill="none" stroke="#222" stroke-width="1.3"><line x1="1" y1="5" x2="16" y2="5"/><polyline points="12,1 16,5 12,9"/></svg>
    </div>
    <div class="service" style="left:558px">
      <svg width="46" height="42" viewBox="0 0 46 42" fill="none" stroke="var(--green)" stroke-width="2.4"><rect x="2" y="10" width="42" height="30"/><path d="M15 10V3h16v7"/></svg>
      <h3>For Companies</h3>
      <p>Fusce facilisis nec ante et accumsan. Ut malesuada tristique sagittis</p>
      <svg class="more" width="18" height="10" viewBox="0 0 18 10" fill="none" stroke="#222" stroke-width="1.3"><line x1="1" y1="5" x2="16" y2="5"/><polyline points="12,1 16,5 12,9"/></svg>
    </div>
    <div class="service" style="left:792px">
      <svg width="46" height="42" viewBox="0 0 46 42" fill="none" stroke="var(--green)" stroke-width="2.6"><polyline points="30,8 6,8 6,38 36,38 36,22"/><polyline points="12,20 20,30 38,2"/></svg>
      <h3>Kick Up Your Career</h3>
      <p>Fusce facilisis nec ante et accumsan. Ut malesuada tristique sagittis</p>
      <svg class="more" width="18" height="10" viewBox="0 0 18 10" fill="none" stroke="#222" stroke-width="1.3"><line x1="1" y1="5" x2="16" y2="5"/><polyline points="12,1 16,5 12,9"/></svg>
    </div>
  </section>

  <section class="abs testimonial">
    <blockquote>Praesent cursus nulla non arcu tempor, ut egestas elit tempus. In ac ex fermentum, gravida felis nec, tincidunt ligula. Sed dapibus mauris ullamcorper.
      <cite>— MARA VELL</cite>
    </blockquote>
  </section>

  <h2 class="abs about-title">About Me</h2>
  <div class="abs portrait" role="img" aria-label="Portrait photo of the coach at an event"></div>
  <h3 class="abs profile-name" style="font-weight:400">Your Name</h3>
  <p class="abs profile-role">A personal mentor</p>
  <p class="abs profile-bio">Sed iaculis dapibus tellus eget condimentum. Curabitur ut tellus congue,</p>
</body>
</html>
```